Business card design for Bront Engineering Qavo

We need a new business card design along with all the necessary to place an order. The company is Bront Engineering Qavo and we recently updated our logo.

```html
<!DOCTYPE html>
<html lang="en">
<head>
<meta charset="utf-8">
<title>Bront Engineering Qavo – Business Card</title>
<link rel="stylesheet" href="https://fonts.googleapis.com/css2?family=Roboto:wght@400;500&display=swap">
<style>
  :root {
    --page: #ffffff;
    --card: #0a0a0a;
    --card-mist: #1c1c1c;
    --yellow: #e3bd22;
    --grey: #8d8d8d;
    --text: #d6d6d6;
  }
  * { box-sizing: border-box; margin: 0; padding: 0; }
  html, body {
    width: 1200px;
    height: 1125px;
    overflow: hidden;
    background: var(--page);
    font-family: "Roboto", Arial, sans-serif;
  }
  .sheet {
    position: relative;
    width: 1200px;
    height: 1125px;
  }
  .card {
    position: absolute;
    left: 160px;
    width: 880px;
    height: 503px;
    border-radius: 60px;
    overflow: hidden;
    background:
      radial-gradient(ellipse 420px 260px at 30% 25%, var(--card-mist), transparent 70%),
      radial-gradient(ellipse 380px 240px at 75% 80%, #161616, transparent 70%),
      var(--card);
  }
  .card--front { top: 40px; }
  .card--back  { top: 582px; }

  /* edge bands */
  .band {
    position: absolute;
    top: 0;
    bottom: 0;
  }
  .card--front .band--yellow { right: 0; width: 22px; background: var(--yellow); }
  .card--front .band--grey   { right: 36px; width: 14px; background: var(--grey); }
  .card--back .band--yellow  { left: 0; width: 22px; background: var(--yellow); }
  .card--back .band--grey    { left: 36px; width: 14px; background: var(--grey); }

  /* front wordmark */
  .wordmark {
    position: absolute;
    left: 142px;
    top: 222px;
    display: flex;
    align-items: center;
    gap: 18px;
  }
  .wordmark__square {
    width: 26px;
    height: 26px;
    background: var(--yellow);
  }
  .wordmark__name {
    font-size: 44px;
    font-weight: 500;
    color: var(--grey);
    letter-spacing: 0.5px;
    white-space: nowrap;
  }

  /* back details */
  .person {
    position: absolute;
    right: 90px;
    top: 100px;
    text-align: right;
  }
  .person__name {
    font-size: 40px;
    font-weight: 500;
    color: var(--yellow);
    line-height: 1;
  }
  .person__role {
    margin-top: 10px;
    font-size: 15px;
    font-weight: 500;
    color: var(--yellow);
    letter-spacing: 6px;
    margin-right: -6px;
  }
  .contacts {
    position: absolute;
    right: 90px;
    top: 208px;
    list-style: none;
    color: var(--text);
    font-size: 21px;
    line-height: 1.3;
  }
  .contacts__row {
    display: flex;
    justify-content: flex-end;
    align-items: center;
    gap: 22px;
    text-align: right;
  }
  .contacts__row--address { margin-bottom: 18px; }
  .contacts__row + .contacts__row { margin-top: 5px; }
  .contacts__icon {
    width: 24px;
    height: 24px;
    flex: none;
    fill: var(--yellow);
  }
</style>
</head>
<body>
<main class="sheet">
  <section class="card card--front" aria-label="Card front">
    <div class="wordmark">
      <span class="wordmark__square"></span>
      <span class="wordmark__name">Bront Engineering Qavo</span>
    </div>
    <span class="band band--grey"></span>
    <span class="band band--yellow"></span>
  </section>

  <section class="card card--back" aria-label="Card back">
    <span class="band band--yellow"></span>
    <span class="band band--grey"></span>

    <div class="person">
      <p class="person__name">Lena Whitcombe</p>
      <p class="person__role">DIRECTOR</p>
    </div>

    <ul class="contacts">
      <li class="contacts__row contacts__row--address">
        <span>Bront Engineering Qavo<br>22b Harwell Road, Kettering NN15 4TR</span>
        <svg class="contacts__icon" viewBox="0 0 24 24" aria-hidden="true"><path d="M12 2a7 7 0 0 0-7 7c0 5 7 13 7 13s7-8 7-13a7 7 0 0 0-7-7zm0 9.5A2.5 2.5 0 1 1 12 6.5a2.5 2.5 0 0 1 0 5z"/></svg>
      </li>
      <li class="contacts__row">
        <span>01536 480273</span>
        <svg class="contacts__icon" viewBox="0 0 24 24" aria-hidden="true"><path d="M3 8c0-2 4-4 9-4s9 2 9 4v2h-5V8.5c-1-.6-2.5-.9-4-.9s-3 .3-4 .9V10H3zm4 3h10l3 8H4zm5 2a2.5 2.5 0 1 0 0 5 2.5 2.5 0 0 0 0-5z"/></svg>
      </li>
      <li class="contacts__row">
        <span>sales@brontengineering.co.uk</span>
        <svg class="contacts__icon" viewBox="0 0 24 24" aria-hidden="true"><path d="M3 5h18v14H3zm2 2v.5l7 5 7-5V7zm0 3v7h14v-7l-7 5z"/></svg>
      </li>
      <li class="contacts__row">
        <span>www.brontengineering.co.uk</span>
        <svg class="contacts__icon" viewBox="0 0 24 24" aria-hidden="true"><path d="M12 2a10 10 0 1 0 0 20 10 10 0 0 0 0-20zm0 2c1 0 2 1.6 2.6 4H9.4C10 5.6 11 4 12 4zM4.5 10h4.6a17 17 0 0 0 0 4H4.5a8 8 0 0 1 0-4zm6.6 0h1.8v4h-1.8a15 15 0 0 1 0-4zm3.8 0h4.6a8 8 0 0 1 0 4h-4.6a17 17 0 0 0 0-4zM9.4 16h5.2c-.6 2.4-1.6 4-2.6 4s-2-1.6-2.6-4z"/></svg>
      </li>
    </ul>
  </section>
</main>
</body>
</html>
```